Criação de Logo e Papelaria (6 itens) para Esportes
" Nós somos um escritório especialista em gestir carreiras de atletas de futebol, sou empresario de futebol . "

```html
<!DOCTYPE html>
<html lang="pt-BR">
<head>
<meta charset="utf-8">
<title>Papel Timbrado — Valdez Group</title>
<link href="https://fonts.googleapis.com/css2?family=Montserrat:wght@500;700&display=swap" rel="stylesheet">
<style>
  :root {
    --backdrop: #8b8b8b;
    --paper: #ffffff;
    --gold: #c9a35a;
    --gold-light: #ecd49a;
    --gold-dark: #a8843e;
    --ink: #1a1a1a;
    --muted: #555555;
    --title: #ffffff;
  }
  html, body {
    margin: 0;
    padding: 0;
    width: 1200px;
    height: 1200px;
    overflow: hidden;
    background: var(--backdrop);
    font-family: "Montserrat", sans-serif;
  }
  .canvas {
    position: relative;
    width: 1200px;
    height: 1200px;
  }
  .sheet-title {
    position: absolute;
    top: 72px;
    left: 0;
    width: 100%;
    margin: 0;
    text-align: center;
    color: var(--title);
    font-weight: 700;
    font-size: 42px;
    letter-spacing: 1px;
  }
  .letterhead {
    position: absolute;
    left: 252px;
    top: 149px;
    width: 691px;
    height: 907px;
    background: var(--paper);
    box-shadow: 6px 10px 18px rgba(0, 0, 0, 0.35);
    overflow: hidden;
  }
  .brand {
    position: absolute;
    top: 76px;
    left: 0;
    width: 100%;
    text-align: center;
    color: var(--gold);
    font-weight: 500;
    font-size: 28px;
    letter-spacing: 1px;
  }
  .contacts {
    position: absolute;
    left: 50px;
    top: 732px;
    margin: 0;
    padding: 0;
    list-style: none;
  }
  .contact {
    display: flex;
    align-items: center;
    height: 24px;
    margin-bottom: 11px;
    font-size: 11px;
    font-weight: 500;
    color: var(--muted);
  }
  .contact-icon {
    width: 20px;
    height: 20px;
    margin-right: 12px;
    flex: none;
  }
  .footer-bands {
    position: absolute;
    left: 0;
    bottom: 0;
    width: 691px;
    height: 40px;
  }
</style>
</head>
<body>
<main class="canvas">
  <h1 class="sheet-title">PAPEL TIMBRADO</h1>

  <section class="letterhead">
    <div class="brand">VALDEZ GROUP</div>

    <ul class="contacts">
      <li class="contact">
        <svg class="contact-icon" viewBox="0 0 20 20" fill="none" stroke="var(--gold)" stroke-width="1.6">
          <path d="M5 3h3l1.5 4-2 1.5a9 9 0 0 0 4 4l1.5-2 4 1.5v3a2 2 0 0 1-2 2A14 14 0 0 1 3 5a2 2 0 0 1 2-2z"/>
        </svg>
        <span>(11) 9000-0000</span>
      </li>
      <li class="contact">
        <svg class="contact-icon" viewBox="0 0 20 20" fill="none" stroke="var(--gold)" stroke-width="1.6">
          <circle cx="10" cy="10" r="7"/>
        </svg>
        <span>@valdezgroup</span>
      </li>
      <li class="contact">
        <svg class="contact-icon" viewBox="0 0 20 20" fill="none" stroke="var(--gold)" stroke-width="1.6">
          <path d="M10 18s-5-5.5-5-9a5 5 0 0 1 10 0c0 3.5-5 9-5 9z"/>
          <circle cx="10" cy="9" r="1.8"/>
        </svg>
        <span>Rua das Palmeiras, 10</span>
      </li>
      <li class="contact">
        <svg class="contact-icon" viewBox="0 0 20 20" fill="none" stroke="var(--gold)" stroke-width="1.6">
          <rect x="3" y="5" width="14" height="10" rx="1"/>
          <path d="M3 6l7 5 7-5"/>
        </svg>
        <span>contato@valdez.com</span>
      </li>
    </ul>

    <svg class="footer-bands" viewBox="0 0 691 40" preserveAspectRatio="none">
      <defs>
        <linearGradient id="goldBand" x1="0" y1="0" x2="1" y2="0">
          <stop offset="0" stop-color="var(--gold-dark)"/>
          <stop offset="0.5" stop-color="var(--gold-light)"/>
          <stop offset="1" stop-color="var(--gold)"/>
        </linearGradient>
      </defs>
      <polygon points="0,6 472,6 456,20 0,20" fill="url(#goldBand)"/>
      <polygon points="462,18 691,12 691,26 452,26" fill="var(--ink)"/>
    </svg>
  </section>
</main>
</body>
</html>
```